Pharmacy handmade, Personalized Medical Cosmetics Label

Medical Cosmetics label, elegant and professional looking. The creams are Dermatologist formulated and are prepared by local Pharmacy. The label should be versatile and allow space for hand writing to be filled by the pharmacist preparing the product.
The following information will be handwritten:
Upper lid - Lid Soothe No.3 ; Marigold, Retinol ; 30
Lower Bottom - Teodora Brandt ; Signature ; 01.01.2017
Upper Lid Label
Vella Skin (logo)
Clinic Series
(circular pattern - Doctor Formulated, Registered Pharmacy, Handmade, Highest Medical Standards)
(Lid Soothe No.3 - in hand writing and different color, maybe red)
Key Ingredients: (Marigold, Retinol - in hand writing, same color as above, maybe red)
(box with hand writing 30) ml
Lower Bottom Label (underneath surface of the container)
Made for Vella Skin by
Pharmacy Estrel, 7 Kalina blvd., Sofia, ph. 0893517640
Patient: (Teodora Brandt- in hand writing)
Pharmacist: (Signature - in hand writing)
Date: (01.01.2017 - in hand writing)
For External Use
good for 60 days after preparation
Ingredients: Retinol, Marigold Extract, Water, Glycerin, Stearyl Alcohol, Wheat Germ Oil, Polysorbate 60, Sesame Oil, Myristyl Myristate, Cetyl Alcohol, Sorbitan Stearate, Phenoxyethanol, Calendula Extract, Cornflower Extract, Sodium Alginate, Sodium Citrate.
The container lid and bottom are 5 cm = 50 mm in diameter. Made from aluminum and contain 30ml or 50ml.
Please refer to the screen shots from my Web Site to get the feeling for the color pallet and professional look. These creams will be sold on this website. They are custom made by a registered Pharmacy right on the spot after the order has been placed. This is why I need more space for the hand written notes made by the pharmacist who prepared the order.
Please make the design professional, simple and serious colors, like light brown, beige, black or dark brown letters, red hand writing (will be filled by pen or thin marker by the Pharmacist by hand, depending on the order, patient name, etc.)
Thank you.
Target Market(s)
female 24 - 49 year old
Industry/Entity Type
Medical

```html
<!DOCTYPE html>
<html lang="en">
<head>
<meta charset="utf-8">
<title>Vella Skin – Clinic Series Labels</title>
<link rel="stylesheet" href="https://fonts.googleapis.com/css2?family=Kaushan+Script&family=Raleway:wght@300;400;600;700&display=swap">
<style>
  :root {
    --bg: #e8e8e8;
    --paper: #ffffff;
    --rim: #c9c9c9;
    --brown-dark: #4a3c38;
    --brown-rule: #8b6a55;
    --ink: #3a3a3a;
    --ink-soft: #6f6f6f;
    --hand-red: #a3201f;
    --panel-grey: #8c8480;
  }
  html, body {
    margin: 0;
    padding: 0;
    width: 1200px;
    height: 820px;
    overflow: hidden;
    background: var(--bg);
  }
  .sheet {
    width: 1200px;
    height: 820px;
    display: flex;
    align-items: center;
    justify-content: space-around;
  }
  .label { width: 540px; height: 540px; display: block; }
  .hand { font-family: "Kaushan Script", cursive; fill: var(--hand-red); }
  .ring-text { font-family: "Raleway", sans-serif; font-weight: 400; font-size: 22px; letter-spacing: 1px; fill: var(--ink); }
  .brand { font-family: "Raleway", sans-serif; font-weight: 400; font-size: 32px; fill: var(--paper); }
  .series { font-family: "Raleway", sans-serif; font-weight: 400; font-size: 22px; letter-spacing: 1px; fill: var(--ink); }
  .key-title { font-family: "Raleway", sans-serif; font-size: 21px; letter-spacing: 1px; fill: var(--ink); }
  .unit { font-family: "Raleway", sans-serif; font-size: 24px; fill: var(--ink); }
  .maker { font-family: "Raleway", sans-serif; font-size: 15px; fill: var(--paper); }
  .maker-strong { font-weight: 700; }
  .field-label { font-family: "Raleway", sans-serif; font-size: 13px; letter-spacing: .5px; fill: var(--ink-soft); }
  .usage { font-family: "Raleway", sans-serif; font-weight: 700; font-size: 13.5px; fill: var(--ink-soft); }
  .ingredients { font-family: "Raleway", sans-serif; font-size: 13.5px; fill: var(--paper); }
  .ingredients-strong { font-weight: 700; }
</style>
</head>
<body>
<main class="sheet">

  <svg class="label label-bottom" viewBox="0 0 540 540" aria-label="Bottom label with patient details">
    <defs>
      <clipPath id="bottom-face"><circle cx="270" cy="270" r="255"/></clipPath>
    </defs>
    <circle cx="270" cy="270" r="268" fill="var(--paper)" stroke="var(--rim)" stroke-width="2"/>
    <g clip-path="url(#bottom-face)">
      <rect x="0" y="0" width="540" height="140" fill="var(--brown-dark)"/>
      <rect x="0" y="352" width="540" height="200" fill="var(--panel-grey)"/>
    </g>

    <g class="maker-block" text-anchor="middle">
      <text class="maker maker-strong" x="270" y="72">Made for Vella Skin</text>
      <text class="maker" x="270" y="96"><tspan class="maker-strong">by:</tspan> Pharmacy Estrel, 7 Kalina blvd.,</text>
      <text class="maker" x="270" y="120">Sofia, ph. 0893517640</text>
    </g>

    <g class="fields">
      <text class="field-label" x="42" y="196">PATIENT:</text>
      <text class="hand" x="122" y="188" font-size="34">Teodora Brandt</text>
      <line x1="40" y1="200" x2="500" y2="200" stroke="var(--rim)" stroke-width="1.5"/>

      <text class="field-label" x="30" y="256">PHARMACIST:</text>
      <text class="hand" x="142" y="248" font-size="34">Lina Petrova</text>
      <line x1="28" y1="260" x2="512" y2="260" stroke="var(--rim)" stroke-width="1.5"/>

      <text class="field-label" x="30" y="316">DATE:</text>
      <text class="hand" x="150" y="308" font-size="34">1.01.2017</text>
      <line x1="28" y1="320" x2="512" y2="320" stroke="var(--rim)" stroke-width="1.5"/>
    </g>

    <text class="usage" x="270" y="342" text-anchor="middle">FOR EXTERNAL USE: GOOD 60 DAYS AFTER PREPARATION</text>

    <g class="ingredient-list" text-anchor="middle">
      <text class="ingredients" x="270" y="378"><tspan class="ingredients-strong">Ingredients:</tspan> Retinol, Marigold Extract, Water, Glycerin,</text>
      <text class="ingredients" x="270" y="399">Stearyl Alcohol, Wheat Germ Oil, Polysorbate 60,</text>
      <text class="ingredients" x="270" y="420">Sesame Oil, Myristyl Myristate, Cetyl Alcohol,</text>
      <text class="ingredients" x="270" y="441">Sorbitan Stearate, Phenoxyethanol, Calendula</text>
      <text class="ingredients" x="270" y="462">Extract, Cornflower Extract, Sodium</text>
      <text class="ingredients" x="270" y="483">Alginate, Sodium Citrate.</text>
    </g>
  </svg>

  <svg class="label label-lid" viewBox="0 0 540 540" aria-label="Lid label with product name">
    <defs>
      <path id="lid-ring-path" d="M 100.3,439.7 A 240 240 0 1 1 439.7,100.3 A 240 240 0 1 1 100.3,439.7"/>
      <clipPath id="lid-face"><circle cx="270" cy="270" r="213"/></clipPath>
    </defs>

    <circle cx="270" cy="270" r="268" fill="var(--paper)" stroke="var(--rim)" stroke-width="2"/>

    <g class="ring-claims">
      <text class="ring-text"><textPath href="#lid-ring-path" startOffset="18%" text-anchor="middle">Highest Medical Standards</textPath></text>
      <text class="ring-text"><textPath href="#lid-ring-path" startOffset="37.5%" text-anchor="middle">Doctor Formulated</textPath></text>
      <text class="ring-text"><textPath href="#lid-ring-path" startOffset="61%" text-anchor="middle">Registered Pharmacy</textPath></text>
      <text class="ring-text"><textPath href="#lid-ring-path" startOffset="87.5%" text-anchor="middle">Handmade</textPath></text>
    </g>

    <g clip-path="url(#lid-face)">
      <rect x="0" y="0" width="540" height="148" fill="var(--brown-dark)"/>
      <rect x="0" y="154" width="118" height="16" fill="var(--brown-dark)"/>
      <rect x="422" y="154" width="118" height="16" fill="var(--brown-dark)"/>
      <rect x="0" y="448" width="540" height="100" fill="var(--brown-dark)"/>
    </g>
    <circle cx="270" cy="270" r="215" fill="none" stroke="var(--brown-rule)" stroke-width="3"/>

    <g class="brand-lockup">
      <circle cx="190" cy="108" r="14" fill="none" stroke="var(--paper)" stroke-width="2"/>
      <text class="brand" x="214" y="119">Vella Skin</text>
    </g>

    <text class="series" x="270" y="170" text-anchor="middle">CLINIC SERIES</text>

    <text class="hand" x="270" y="262" font-size="48" text-anchor="middle">Lid Soothe No.3</text>
    <line x1="70" y1="296" x2="470" y2="296" stroke="var(--ink)" stroke-width="1"/>
    <text class="key-title" x="270" y="328" text-anchor="middle">KEY INGREDIENTS</text>
    <text class="hand" x="270" y="384" font-size="44" text-anchor="middle">Marigold, Retinol</text>
    <text x="270" y="430" text-anchor="middle"><tspan class="hand" font-size="28">30</tspan><tspan class="unit" dx="6">ml</tspan></text>
  </svg>

</main>
</body>
</html>
```